Aisle signage for supermarket

Design Isle signs for Indian supermarket. Modern, Clear, legible. Would be nice to use our logo colours. Signs Will be double sided and measure 900mm width x 400mm height. Indian theme would be nice. Attached files shows description to go on each sign.
Font styles to use
Sans Serif
Colors
Designer to choose colors to be used in the design.

```html
<!DOCTYPE html>
<html lang="en">
<head>
<meta charset="utf-8">
<title>Aisle 1 Sign</title>
<link rel="stylesheet" href="https://fonts.googleapis.com/css2?family=Arimo:wght@700&display=swap">
<style>
  :root {
    --backdrop: #3b3b3b;
    --sign-green: #56b037;
    --band-green: #7cc461;
    --panel-white: #ffffff;
    --ink: #000000;
    --brand-green: #1f7a3e;
  }
  html, body {
    margin: 0;
    width: 1200px;
    height: 1200px;
    overflow: hidden;
    background: var(--backdrop);
    font-family: "Arimo", Arial, sans-serif;
  }
  .aisle-sign {
    position: absolute;
    left: 80px;
    top: 369px;
    width: 1040px;
    height: 462px;
    background: var(--sign-green);
    overflow: hidden;
  }
  .aisle-sign__panel {
    position: absolute;
    inset: 0;
  }
  .brand {
    position: absolute;
    left: 22px;
    top: 58px;
    width: 205px;
    color: var(--brand-green);
    font-weight: 700;
    text-align: center;
  }
  .brand__name {
    display: block;
    font-size: 40px;
    letter-spacing: 10px;
    line-height: 1;
    margin-right: -10px;
  }
  .brand__tag {
    display: flex;
    align-items: center;
    gap: 6px;
    font-size: 9px;
    letter-spacing: 4px;
    margin-top: 6px;
  }
  .brand__tag::before,
  .brand__tag::after {
    content: "";
    flex: 1;
    height: 1px;
    background: var(--ink);
  }
  .aisle-number {
    position: absolute;
    left: 18px;
    width: 200px;
    top: 108px;
    font-size: 328px;
    line-height: 1;
    font-weight: 700;
    color: var(--ink);
    text-align: center;
  }
  .categories {
    position: absolute;
    left: 350px;
    width: 640px;
    top: 0;
    height: 100%;
  }
  .category {
    position: absolute;
    left: 0;
    right: 0;
    text-align: center;
    font-size: 74px;
    font-weight: 700;
    line-height: 1;
    color: var(--ink);
    white-space: nowrap;
  }
  .category--1 { top: 91px; }
  .category--2 { top: 214px; }
  .category--3 { top: 336px; }
  .divider {
    position: absolute;
    left: 0;
    right: 0;
    height: 3px;
    background: var(--panel-white);
    border-radius: 2px;
  }
  .divider::before,
  .divider::after {
    content: "";
    position: absolute;
    top: -6px;
    width: 12px;
    height: 12px;
    background: var(--panel-white);
    transform: rotate(45deg);
  }
  .divider::before { left: -4px; }
  .divider::after { right: -4px; }
  .divider--1 { top: 183px; }
  .divider--2 { top: 306px; }
</style>
</head>
<body>
  <div class="aisle-sign">
    <svg class="aisle-sign__panel" width="1040" height="462" viewBox="0 0 1040 462">
      <circle class="ornament-band" cx="-11" cy="216" r="335" fill="var(--band-green)" role="img" aria-label="White scrollwork lace border around the number panel"/>
      <circle class="number-panel" cx="-11" cy="216" r="290" fill="var(--panel-white)"/>
    </svg>
    <div class="brand">
      <span class="brand__name">NADIR</span>
      <span class="brand__tag">STORES</span>
    </div>
    <div class="aisle-number">1</div>
    <div class="categories">
      <div class="category category--1">BISCUITS / CAKES</div>
      <div class="divider divider--1"></div>
      <div class="category category--2">TEA / COFFE</div>
      <div class="divider divider--2"></div>
      <div class="category category--3">SAVOURIES</div>
    </div>
  </div>
</body>
</html>
```